Business Card Design

I need a new business card design for myself. I am a life coach and therapist with both a private practice and now a newly formed business see both my websites: I am looking for a business card to support this and be close to the colours and design of my private practice website and my business website. I am looking for strong bright nature based colours. Sun, Sea and Greenery. The card should reflect inspiration, enlightenment, empowerment and strength!!!
www.helenagracewarrick.com and
www.calmer-paths-mentoring.co.uk
Updates
Thank you everyone for your designs. I will be making a final decision by the end of this week and will notify you as soon as possible after this.
Industry/Entity Type
Business
Contact Information for Business Card
Helena Grace Warrick, BSc, PGDip & MRes
Therapist and Life Coach
Calmer Paths Mentoring
17 Larkspur Road
Manchester
M4 7QT
0800 0619483 Mobile: 07700948216
email: hgwarrick@helenagracewarrick.com
Requirements
Must have
- not too busy. To be clear and easy to read information..
and to include this tag line:
"helping you live your life with passion and confidence"

```html
<!DOCTYPE html>
<html lang="en">
<head>
<meta charset="utf-8">
<title>Helena Grace Warrick – Business Card</title>
<link rel="stylesheet" href="https://fonts.googleapis.com/css2?family=Noto+Sans:wght@400&display=swap">
<style>
  :root {
    --leaf-green: #8ad80c;
    --white: #ffffff;
    --forest-deep: #143318;
    --forest-mid: #2f6a25;
    --forest-light: #5fb332;
  }
  html, body {
    margin: 0;
    padding: 0;
    overflow: hidden;
    background: #ffffff;
  }
  .card {
    position: relative;
    width: 1200px;
    height: 791px;
    background: var(--leaf-green);
    overflow: hidden;
    font-family: "Noto Sans", Verdana, sans-serif;
    color: var(--white);
  }
  .card__scenery {
    position: absolute;
    inset: 0;
    width: 1200px;
    height: 791px;
  }
  .card__text {
    position: absolute;
    left: 54px;
    margin: 0;
    white-space: nowrap;
    text-shadow: 0 0 6px rgba(255,255,255,0.55);
    font-weight: 400;
    line-height: 1.2;
  }
  .card__name { top: 176px; font-size: 46px; }
  .card__detail { font-size: 36px; }
  .card__credentials { top: 240px; }
  .card__role { top: 291px; }
  .card__business { top: 343px; }
  .card__contact { font-size: 33px; }
  .card__street { top: 478px; }
  .card__city { top: 525px; }
  .card__mobile { top: 572px; }
  .card__email { top: 619px; }
  .card__tagline { top: 714px; font-size: 25px; }
</style>
</head>
<body>
  <div class="card">
    <svg class="card__scenery" viewBox="0 0 1200 791" xmlns="http://www.w3.org/2000/svg" role="img" aria-label="Photograph of a tall waterfall dropping into a pool surrounded by lush tropical rainforest and ferns">
      <defs>
        <linearGradient id="forest" x1="0" y1="0" x2="1" y2="1">
          <stop offset="0" stop-color="var(--forest-deep)"/>
          <stop offset="0.5" stop-color="var(--forest-mid)"/>
          <stop offset="1" stop-color="var(--forest-light)"/>
        </linearGradient>
      </defs>
      <polygon points="450,0 1200,0 1200,791 932,791" fill="url(#forest)"/>
    </svg>

    <p class="card__text card__name">Helena Grace Warrick</p>
    <p class="card__text card__detail card__credentials">BSc, PGDip &amp; MRes</p>
    <p class="card__text card__detail card__role">Therapist and Life Coach</p>
    <p class="card__text card__detail card__business">Calmer Paths Mentoring</p>

    <p class="card__text card__contact card__street">17 Larkspur Road</p>
    <p class="card__text card__contact card__city">Manchester M4 7QT 0800 0619483</p>
    <p class="card__text card__contact card__mobile">Mobile: 07700948216</p>
    <p class="card__text card__contact card__email">email: hgwarrick@helenagracewarrick.com</p>

    <p class="card__text card__tagline">"helping you live your life with passion and confidence"</p>
  </div>
</body>
</html>
```